Amber Hollow Sweets Business Card Design

Need a business card design for my eco-luxe dessert company Amber Hollow Sweets. The cards will be printed on 100% post consumer recycled content... so some kind of natural colored paper.

Two sided
Standard Size 2" x 3.5"

Front Content:
Logo
Local. Seasonal. Organic. (underneath logo)

Back Content:
Marla Quince
Seasonal Pastry Chef
Alderwick, Connecticut

www.amberhollowsweets.example
amberhollowsweets@mailbox.example
203-571-3064

QR Code (file image)

The cards are going to be printed on recycled paper similar to this color:
HEX: #D5BC84
RGB: 213/188/132

Target Market(s)

Eco-Conscious
Educated
Wealthy
Foodies

Industry/Entity Type

Business

Requirements
Must have
• Two sided Business Card
Standard Size 2" x 3.5"

Front Content:
Logo

Back Content:
Marla Quince
Seasonal Pastry Chef
203-571-3064
www.amberhollowsweets.example
Alderwick, Connecticut
*There will also be a QR code. When submitting designs please leave room for the code on the back and I will post the url for the code shortly.
Nice to have
• Earthy Colors (green, brown) with some vibrant oranges/gold

```html
<!DOCTYPE html>
<html lang="en">
<head>
<meta charset="utf-8">
<title>Amber Hollow Sweets – Business Card</title>
<link rel="stylesheet" href="https://fonts.googleapis.com/css2?family=Arimo:ital,wght@0,400;0,700;1,400&display=swap">
<style>
  :root {
    --page: #ffffff;
    --paper: #d6bd86;
    --bark: #4a2b23;
    --ink: #3d2a22;
    --leaf: #9a9a2c;
  }
  * { box-sizing: border-box; margin: 0; padding: 0; }
  html, body {
    width: 1200px;
    height: 900px;
    overflow: hidden;
    background: var(--page);
    font-family: "Arimo", Arial, sans-serif;
  }
  .canvas {
    position: relative;
    width: 1200px;
    height: 900px;
  }
  .card {
    position: absolute;
    top: 70px;
    width: 426px;
    height: 740px;
    background: var(--paper);
    border-top: 24px solid var(--bark);
    border-bottom: 22px solid var(--bark);
    color: var(--ink);
  }
  .card--front { left: 166px; }
  .card--back { left: 636px; }

  /* Front */
  .brand-mark {
    position: absolute;
    left: 50%;
    top: 186px;
    width: 130px;
    height: 130px;
    margin-left: -65px;
    border-radius: 50%;
    background: var(--leaf);
  }
  .brand-name {
    position: absolute;
    left: 0;
    right: 0;
    top: 350px;
    text-align: center;
    font-size: 32px;
    font-weight: 400;
    letter-spacing: 0.5px;
    color: var(--bark);
  }
  .brand-rule {
    position: absolute;
    left: 38px;
    right: 50px;
    top: 420px;
    height: 2px;
    background: var(--bark);
  }
  .tagline {
    position: absolute;
    left: 0;
    right: 0;
    top: 430px;
    text-align: center;
    font-size: 22px;
    font-weight: 700;
    letter-spacing: 0.6px;
    color: var(--bark);
  }

  /* Back */
  .contact {
    position: absolute;
    left: 0;
    right: 0;
    top: 166px;
    text-align: center;
    font-size: 20px;
    line-height: 25px;
  }
  .contact__name { font-weight: 700; }
  .contact__role { font-style: italic; }
  .contact__city { font-weight: 700; }
  .contact__links { margin-top: 26px; font-size: 19px; line-height: 26px; }
  .contact__label { font-weight: 700; }
  .contact__phone { margin-top: 20px; font-weight: 700; font-size: 20px; }
  .back-mark {
    position: absolute;
    left: 50%;
    top: 512px;
    width: 150px;
    height: 150px;
    margin-left: -75px;
    border-radius: 50%;
    background: var(--leaf);
  }
</style>
</head>
<body>
<div class="canvas">
  <section class="card card--front" aria-label="Card front">
    <div class="brand-mark" aria-hidden="true"></div>
    <h1 class="brand-name">Amber Hollow Sweets</h1>
    <div class="brand-rule" aria-hidden="true"></div>
    <p class="tagline">Local. Seasonal. Organic.</p>
  </section>

  <section class="card card--back" aria-label="Card back">
    <div class="contact">
      <p class="contact__name">Marla Quince</p>
      <p class="contact__role">Seasonal Pastry Chef</p>
      <p class="contact__city">Alderwick, Connecticut</p>
      <div class="contact__links">
        <p><span class="contact__label">w:</span> www.amberhollowsweets.example</p>
        <p><span class="contact__label">e:</span> amberhollowsweets@mailbox.example</p>
      </div>
      <p class="contact__phone">203-571-3064</p>
    </div>
    <div class="back-mark" aria-hidden="true"></div>
  </section>
</div>
</body>
</html>
```